Aged Care Home - TP

We need a website design for a homepage and a content page for an aged care home in Brisbane. I have attached a detailed design/content brief and their logo to be used in concepts. Also bear in mind this design will be skinned for Dot Net Nuke 4.8.2 so design needs to be used on this content management system.

The following elements are required in the design:

• Phone number will be featured in banner on each page 07 5281 6372

• An area for a large flash banner of rotating images on homepage

• Images need to reflect credibility, professionalism and caring (just use some example images for now as we’ll need to source some)

• Large logo in banner as well

• Some icons on homepage to include:

• Download Application Form

• Admission Kit

• Contact Us

```html
<!DOCTYPE html>
<html lang="en">
<head>
<meta charset="utf-8">
<title>The Thea Parker Home</title>
<link rel="stylesheet" href="https://fonts.googleapis.com/css2?family=Lato:wght@400;700&family=PT+Sans:wght@400;700&display=swap">
<style>
:root{
  --navy:#1c1a6e;
  --lavender:#c9b3ef;
  --purple:#7262c0;
  --purple-deep:#6a5ab8;
  --panel:#cfc3fb;
  --page:#ece6fa;
  --text:#3e3a55;
  --muted:#8d8d99;
  --red:#e1001a;
  --green:#36b82c;
  --white:#ffffff;
}
*{margin:0;padding:0;box-sizing:border-box}
html,body{width:1200px;height:938px;overflow:hidden;background:var(--white)}
body{position:relative;font-family:"PT Sans",Arial,sans-serif;color:var(--text)}
.site-header{position:absolute;left:0;top:0;width:1200px;height:230px;background:var(--white)}
.brand{position:absolute;left:110px;top:66px;display:flex;align-items:center;gap:22px}
.brand-mark{width:34px;height:34px;border-radius:50%;background:var(--navy)}
.brand-name{font-family:"Lato",sans-serif;font-weight:400;font-size:44px;color:var(--navy);letter-spacing:.5px}
.welcome{position:absolute;right:36px;top:192px;font-family:"Lato",sans-serif;font-size:17px;letter-spacing:2.6px;color:var(--lavender)}
.hero-band{position:absolute;left:0;top:230px;width:1200px;height:281px;
  background:linear-gradient(180deg,#d2c4f0 0%,#b3a3e6 30%,#8576cc 65%,var(--purple-deep) 100%)}
.hero-feature{position:absolute;left:0;top:0;width:370px;height:281px;
  background:linear-gradient(135deg,#d9cff5 0%,#a495dc 45%,#6b5bb4 100%)}
.banner-frame{position:absolute;left:328px;top:25px;width:852px;height:142px;background:var(--white);border-radius:10px}
.banner-slide{position:absolute;left:8px;top:8px;width:836px;height:125px;border-radius:4px;
  background:linear-gradient(90deg,#2d5e9c 0%,#6b97c7 30%,#c8dbee 60%,#f4f7fb 80%,#ffffff 100%)}
.banner-slide::after{content:"";position:absolute;left:0;bottom:0;width:60%;height:22px;
  background:linear-gradient(90deg,#4f8a2e,#8fbd5c 70%,rgba(255,255,255,0))}
.banner-name{position:absolute;right:34px;top:24px;font-family:"Lato",sans-serif;font-size:30px;color:var(--navy)}
.banner-phone{position:absolute;right:28px;top:64px;font-family:"Lato",sans-serif;font-size:22px;letter-spacing:3px;color:var(--navy)}
.main-nav{position:absolute;right:28px;top:248px;display:flex;align-items:center;font-size:16px;color:var(--white)}
.main-nav a{color:var(--white);text-decoration:none;padding:0 18px}
.main-nav a.active{font-weight:700}
.main-nav .sep{width:2px;height:14px;background:var(--green)}
.content{position:absolute;left:0;top:511px;width:1200px;height:343px;
  background:linear-gradient(180deg,#f1ecfd 0%,var(--page) 60%,#ddd4f5 100%)}
.intro{position:absolute;left:22px;top:42px;width:647px;height:257px;background:var(--panel);border-radius:8px}
.intro-photo{position:absolute;left:41px;top:28px;width:297px;height:100px;
  background:linear-gradient(180deg,#9fa07a 0%,#b76b4a 40%,#7a2a20 70%,#c7684a 100%)}
.intro p{position:absolute;font-size:11.3px;line-height:16.5px;color:#4b4763;text-align:justify}
.intro .col-left{left:37px;top:142px;width:302px}
.intro .col-right{left:385px;top:22px;width:241px}
.intro .col-right span{display:block;margin-bottom:16px}
.card{position:absolute;width:243px;height:124px;background:var(--white);border:1px solid #c9c3d8;border-radius:7px}
.card-icon{position:absolute;left:8px;top:10px}
.card-photo{position:absolute;left:52px;top:5px;width:184px;height:50px;border-radius:6px}
.card h3{position:absolute;left:0;top:58px;width:100%;padding-left:20px;text-align:center;font-size:12px;font-weight:700;letter-spacing:.5px;color:var(--red)}
.card p{position:absolute;left:10px;top:72px;width:226px;font-size:10.4px;line-height:12.5px;color:var(--muted);text-align:center}
.card .more{position:absolute;right:12px;bottom:5px;font-size:10px;font-weight:700;color:var(--red)}
.card-1{left:692px;top:43px}
.card-2{left:940px;top:43px}
.card-3{left:692px;top:173px}
.card-4{left:940px;top:173px}
.photo-room{background:linear-gradient(90deg,#b4501a,#e89a3b 55%,#d8432a)}
.photo-sunset{background:linear-gradient(180deg,#6e3d22 0%,#e2922f 55%,#4a3a40 100%)}
.photo-paper{background:linear-gradient(135deg,#e6ebf2,#b7c4d6 60%,#e9e2c9)}
.photo-snow{background:linear-gradient(135deg,#cfd6e4,#eef1f6 50%,#a9b2c4)}
.site-footer{position:absolute;left:0;top:854px;width:1200px;height:84px;
  background:linear-gradient(180deg,#c2b3ee 0%,#ddd3f7 40%,#ffffff 100%)}
.site-footer p{position:absolute;left:0;top:24px;width:1200px;text-align:center;font-size:11px;color:#8b84ad}
</style>
</head>
<body>
<header class="site-header">
  <div class="brand"><span class="brand-mark"></span><span class="brand-name">THE THEA PARKER HOME</span></div>
  <div class="welcome">Welcome to The Thea Parker Home - On Line</div>
</header>

<section class="hero-band">
  <div class="hero-feature" role="img" aria-label="Hand placing a jigsaw piece over a lavender-toned puzzle with a house"></div>
  <div class="banner-frame">
    <div class="banner-slide" role="img" aria-label="Rotating banner: couple standing on a grassy field under a blue sky beside a drawn house outline"></div>
    <div class="banner-name">THEA PARKER HOME</div>
    <div class="banner-phone">07 5281 6372</div>
  </div>
  <nav class="main-nav">
    <a class="active" href="#">Home</a><span class="sep"></span>
    <a href="#">About</a><span class="sep"></span>
    <a href="#">Accomedation Option</a><span class="sep"></span>
    <a href="#">Contact Us</a><span class="sep"></span>
    <a href="#">Brochurs &amp; Forms</a>
  </nav>
</section>

<main class="content">
  <article class="intro">
    <div class="intro-photo" role="img" aria-label="Brick entrance sign of the home surrounded by garden plants"></div>
    <p class="col-left">The Thea Parker Home, situated in the riverside Brisbane Suburb of Riverbend, has a long history of providing accommodation to people of the community. The Riverbend Hostel, as it was known during World War II, was completely rebuilt in 1979 when the Senior and Disabled Persons Care Association was formed.</p>
    <p class="col-right"><span>Over the years refurbishments and renovations to the home have resulted in the establishment of a modern, comfortable facility which is a registered charitable organization, aligned to no other group and is administered by a voluntary board of directors.</span><span>The facility, on the corner of Harbour Street and Wattle Street, Riverbend and is surrounded by beautiful gardens and has many outdoor areas for recreation and relaxation.</span></p>
  </article>

  <div class="card card-1">
    <svg class="card-icon" width="38" height="38" viewBox="0 0 38 38"><circle cx="19" cy="19" r="17" fill="#5cc23f" stroke="#2f8f22" stroke-width="2"/><circle cx="19" cy="14" r="5" fill="#fff"/><path d="M10 28c1-6 5-8 9-8s8 2 9 8z" fill="#fff"/></svg>
    <div class="card-photo photo-room" role="img" aria-label="Furnished bedroom in warm tones"></div>
    <h3>ACCOMEDATION OPTION</h3>
    <p>We have range of accommodation styles to suit a wide variety of needs. The following types of accommodation are offered</p>
    <span class="more">MORE »»</span>
  </div>
  <div class="card card-2">
    <svg class="card-icon" width="38" height="38" viewBox="0 0 38 38"><circle cx="19" cy="19" r="17" fill="#5cc23f" stroke="#2f8f22" stroke-width="2"/><rect x="11" y="17" width="4" height="11" fill="#fff"/><rect x="17" y="11" width="4" height="17" fill="#fff"/><rect x="23" y="20" width="4" height="8" fill="#fff"/></svg>
    <div class="card-photo photo-sunset" role="img" aria-label="Couple silhouetted against a sunset over water"></div>
    <h3>PHILOSOPHY OF CARE</h3>
    <p>We have range of accommodation styles to suit a wide variety of needs. The following types of accommodation are offered</p>
    <span class="more">MORE »»</span>
  </div>
  <div class="card card-3">
    <svg class="card-icon" width="38" height="38" viewBox="0 0 38 38"><circle cx="19" cy="19" r="17" fill="#5cc23f" stroke="#2f8f22" stroke-width="2"/><rect x="12" y="9" width="14" height="20" fill="#fff"/><path d="M15 14h8M15 18h8M15 22h8" stroke="#2f8f22" stroke-width="1.5"/></svg>
    <div class="card-photo photo-paper" role="img" aria-label="Fountain pen resting on a printed form with charts"></div>
    <h3>DOWNLOAD APPLICATION FORM</h3>
    <p>We have range of accommodation styles to suit a wide variety of needs. The following types of accommodation are offered</p>
    <span class="more">MORE »»</span>
  </div>
  <div class="card card-4">
    <svg class="card-icon" width="38" height="38" viewBox="0 0 38 38"><circle cx="19" cy="19" r="17" fill="#5cc23f" stroke="#2f8f22" stroke-width="2"/><rect x="10" y="13" width="18" height="13" fill="#fff"/><path d="M10 13l9 8 9-8" fill="none" stroke="#2f8f22" stroke-width="1.5"/></svg>
    <div class="card-photo photo-snow" role="img" aria-label="Red mailbox in a snowy landscape"></div>
    <h3>SEND MESSAGE</h3>
    <p>We have range of accommodation styles to suit a wide variety of needs. The following types of accommodation are offered</p>
    <span class="more">MORE »»</span>
  </div>
</main>

<footer class="site-footer">
  <p>Copyright © 2008 AgedCare THEA Parker Home, Tel 07 5281 6372</p>
</footer>
</body>
</html>
```